依頼詳細
弊社のトップページのリニューアルをお願いします。

内容はMRキャップ(弊社メーカーにて販売)とカチモア(ネジ通販サイト)の2点に絞りこみ出来るだけシンプルなデザインにしてほしい。
その他のページの改良は未定ですが、満足いくものが出来れば全面リニューアルの際に
再度ご依頼させて頂きます。
サイトURL
http://www.hanamizucorp.co.jp/
ページ数
1ページ
希望イメージ
シンプル 複雑
単色 カラフル
暗い 明るい
日常 高級
遊び心 厳粛
未来的 伝統的
女性的 男性的
希望する色
青系、水色系、グレー系
納品ファイル
• 高解像度JPG (.jpg)
• イラストレーター形式 (.ai)
• フォトショップ形式 (.psd)
• PNG形式 (.png)
補足説明
画像素材も付けておきます。
宜しくお願いします。
■ 選んだ理由

素晴らしいセンスと柔軟な対応で、気持ちよく進めることが出来ました。
スキルも幅広い方なので、今後ご依頼をさせて頂く際心強いと思い決めさせていただきました。

■ 提案者全員のお礼・コメント

当選決定が遅くなってしまい申し訳ありませんでした。
クオリティの高い画像をありがとうございました。
また機会がありましたら、よろしくお願いいたします。

```html
<!DOCTYPE html>
<html lang="ja">
<head>
<meta charset="utf-8">
<title>株式会社ハナミズ｜ネジ革命を推進する会社</title>
<link href="https://fonts.googleapis.com/css2?family=Noto+Sans+JP:wght@400;700&family=Noto+Serif+JP:wght@400;700&family=Cinzel:wght@400;700&display=swap" rel="stylesheet">
<style>
:root{
  --bg:#e7ebef;
  --bg-deep:#d5dbe2;
  --ink:#333a42;
  --muted:#6d747c;
  --nav:#3a3f45;
  --nav-line:#55595f;
  --blue:#2f6fb5;
  --blue-dark:#1d4f8a;
  --sky:#8fc2e8;
  --white:#ffffff;
  --footer:#f4f6f8;
}
*{margin:0;padding:0;box-sizing:border-box}
html,body{width:1200px;height:2192px;overflow:hidden}
body{font-family:"Noto Sans JP",sans-serif;color:var(--ink);background:linear-gradient(180deg,var(--bg) 0%,var(--bg-deep) 60%,#c8d0d9 100%);position:relative}
.topline{height:18px;font-size:10px;color:var(--muted);padding:3px 24px;background:var(--white)}
.header{height:44px;background:var(--white);display:flex;justify-content:space-between;align-items:center;padding:0 28px}
.brand{display:flex;align-items:center;gap:10px;font-weight:700;font-size:22px;color:var(--blue-dark)}
.brand-mark{width:22px;height:22px;border-radius:50%;background:var(--blue-dark)}
.contact{display:flex;align-items:center;gap:8px;color:#c2272d;font-weight:700;font-size:28px}
.contact small{font-size:11px;color:var(--ink);font-weight:400;display:block;line-height:1.2}
.nav{height:30px;margin:0 24px;background:var(--nav);display:flex}
.nav a{color:var(--white);font-size:12px;text-decoration:none;width:150px;text-align:center;line-height:30px;border-right:1px solid var(--nav-line)}
.hero{margin:0 24px;height:200px;background:radial-gradient(ellipse at 40% 120%,#3d7bb8 0%,#123055 40%,#060d1a 75%);display:flex;flex-direction:column;justify-content:center;align-items:center;color:var(--white)}
.hero h1{font-family:"Noto Serif JP",serif;font-size:34px;letter-spacing:6px;text-shadow:0 2px 6px #000}
.hero p{font-family:"Cinzel",serif;font-size:14px;letter-spacing:3px;margin-top:10px}
.news{margin:22px auto 0;width:900px}
.news li{list-style:none;display:flex;align-items:center;gap:22px;height:36px;border-bottom:1px dotted #b3bac2;font-size:12px}
.tag{background:var(--blue);color:var(--white);font-size:10px;padding:3px 12px;border-radius:2px}
.section-title{text-align:center;font-family:"Cinzel",serif;font-size:34px;color:var(--ink)}
.section-sub{text-align:center;font-size:11px;color:var(--muted);margin-top:2px}
.products{margin-top:56px}
.product-card{width:700px;margin:22px auto 0;background:var(--white);display:flex;padding:28px 40px;gap:30px;box-shadow:0 1px 4px rgba(0,0,0,.12)}
.product-card h3{font-family:"Noto Serif JP",serif;font-size:22px;margin-bottom:14px}
.product-card p{font-size:12px;line-height:1.9;color:var(--muted)}
.product-photo{width:200px;height:140px;flex:none;background:radial-gradient(circle,#c9ced4,#8a9199);border-radius:4px}
.btn{display:block;width:150px;margin:18px auto 0;background:var(--blue);color:var(--white);text-align:center;font-size:12px;padding:8px 0;border-radius:3px;text-decoration:none}
.shopping{margin-top:56px}
.shop-preview{width:1010px;height:462px;margin:22px auto 0;background:linear-gradient(180deg,#eef3f8,#dfe7ef);border:1px solid #b9c2cc}
.shop-link{text-align:center;color:#c2272d;font-size:13px;font-weight:700;margin-top:22px}
.shop-banner{width:760px;height:90px;margin:10px auto 0;background:linear-gradient(90deg,#17345c,#2f6fb5);border-radius:4px;display:flex;align-items:center;justify-content:center;color:var(--white);font-size:34px;font-weight:700;letter-spacing:4px}
.footer{position:absolute;left:0;right:0;bottom:0;height:230px;background:var(--footer);border-top:4px solid var(--blue);display:flex;justify-content:space-between;padding:36px 60px}
.footer .brand{font-size:18px}
.footer address{font-style:normal;font-size:11px;color:var(--muted);line-height:1.8;margin-top:12px}
.footer ul{list-style:none;font-size:12px;line-height:2;columns:2;column-gap:50px}
.copy{position:absolute;bottom:12px;left:0;right:0;text-align:center;font-size:10px;color:var(--muted)}
</style>
</head>
<body>
<div class="topline">ネジ・ボルト・ナットの製造販売｜株式会社ハナミズ</div>
<header class="header">
  <div class="brand"><span class="brand-mark"></span>株式会社ハナミズ</div>
  <div class="contact"><small>TEL/FAX<br>通話無料</small>0120-00-2468</div>
</header>
<nav class="nav"><a>ホーム</a><a>製品情報</a><a>カチモア</a><a>アクセスマップ</a><a>企業情報</a><a>お問い合わせ</a></nav>
<section class="hero" role="img" aria-label="宇宙から見た地球の写真">
  <h1>ネジ革命を推進する会社</h1>
  <p>— COMPANY THAT PROMOTES SCREW REVOLUTION —</p>
</section>
<ul class="news">
  <li><span class="tag">NEWS</span>2014.01.20<span>ネジ通販サイト「カチモア」の新商品を追加しました。</span></li>
  <li><span class="tag">NEWS</span>2014.01.15<span>年末年始の営業日についてご案内します。</span></li>
  <li><span class="tag">NEWS</span>2014.01.10<span>MRキャップのカタログを更新しました。</span></li>
</ul>
<section class="products">
  <h2 class="section-title">Products</h2>
  <p class="section-sub">製品情報</p>
  <div class="product-card">
    <div>
      <h3>MRキャップシリーズ</h3>
      <p>MRキャップは「防錆効果」「省スペース」「優れた外観」を兼ね備えたネジキャップです。ボルトの先端を覆い、安全性と美観を高めます。多彩なサイズをご用意しています。</p>
    </div>
    <div class="product-photo" role="img" aria-label="金属製ネジキャップの製品写真"></div>
  </div>
  <a class="btn">もっと詳しく見る</a>
</section>
<section class="shopping">
  <h2 class="section-title">Shopping</h2>
  <p class="section-sub">カチモア</p>
  <div class="shop-preview" role="img" aria-label="ネジ通販サイト カチモアの画面イメージ"></div>
  <p class="shop-link">▶▶ショッピングサイトはこちら◀◀</p>
  <div class="shop-banner">カチモア</div>
</section>
<footer class="footer">
  <div>
    <div class="brand"><span class="brand-mark"></span>株式会社ハナミズ</div>
    <address>〒000-0000 花水県青葉市緑町1丁目2番3号<br>TEL 0120-00-2468 / FAX 0120-00-2468<br>http://www.hanamizucorp.co.jp/</address>
  </div>
  <ul><li>ホーム</li><li>製品情報</li><li>カチモア</li><li>アクセスマップ</li><li>企業情報</li><li>お問い合わせ</li></ul>
</footer>
<p class="copy">Copyright © Hanamizu Corp. All Rights Reserved.</p>
</body>
</html>
```